Criação de Papelaria Profissional para Advocacia e Direito
A empresa queria:
" Ribeiro Tavares Advogados é um escritório boutique de atuação diversificada (full service) "

```html
<!DOCTYPE html>
<html lang="pt-BR">
<head>
<meta charset="UTF-8">
<title>Ribeiro Tavares Advogados — Cartão</title>
<link rel="stylesheet" href="https://fonts.googleapis.com/css2?family=Montserrat:wght@400;500&family=Open+Sans:wght@400&display=swap">
<style>
  :root {
    --page-bg: #e9e6e2;
    --brand-blue: #3d5a73;
    --divider-grey: #b9babc;
    --card-white: #ffffff;
    --name-grey: #a3a6a9;
    --text-dark: #3a3d40;
    --icon-grey: #6d7074;
    --mark-grey: #d4d6d8;
    --logo-white: #ffffff;
    --logo-sub: #c9d3dc;
  }
  * { margin: 0; padding: 0; box-sizing: border-box; }
  html, body { width: 1200px; height: 1200px; overflow: hidden; }
  body {
    background: var(--page-bg);
    position: relative;
    font-family: "Open Sans", Arial, sans-serif;
  }
  .card {
    position: absolute;
    left: 89px;
    top: 462px;
    width: 1022px;
    height: 276px;
    border-radius: 26px;
    background: var(--brand-blue);
    overflow: hidden;
    box-shadow: 0 6px 18px rgba(0,0,0,0.18);
  }
  .card__divider {
    position: absolute;
    left: 490px;
    top: 0;
    right: 0;
    bottom: 0;
    background: var(--divider-grey);
    border-top-left-radius: 70px;
  }
  .card__info {
    position: absolute;
    left: 516px;
    top: 0;
    right: 0;
    bottom: 0;
    background: var(--card-white);
    border-top-left-radius: 70px;
  }
  .brand {
    position: absolute;
    left: 0;
    top: 74px;
    width: 450px;
    display: flex;
    flex-direction: column;
    align-items: center;
    font-family: "Montserrat", Arial, sans-serif;
  }
  .brand__square {
    width: 40px;
    height: 40px;
    border: 3px solid var(--logo-white);
    margin-bottom: 12px;
  }
  .brand__name {
    color: var(--logo-white);
    font-size: 35px;
    font-weight: 400;
    letter-spacing: 2px;
    line-height: 1;
    white-space: nowrap;
  }
  .brand__tagline {
    margin-top: 9px;
    color: var(--logo-sub);
    font-size: 10px;
    font-weight: 500;
    letter-spacing: 2px;
    text-transform: uppercase;
  }
  .person-name {
    position: absolute;
    left: 566px;
    top: 20px;
    font-size: 33px;
    color: var(--name-grey);
    font-weight: 400;
  }
  .contact-list {
    position: absolute;
    left: 566px;
    top: 76px;
    list-style: none;
  }
  .contact-list__item {
    display: flex;
    align-items: center;
    height: 45px;
    font-size: 21px;
    color: var(--text-dark);
  }
  .contact-list__icon {
    width: 24px;
    height: 24px;
    margin-right: 16px;
    flex: none;
  }
  .faint-mark {
    position: absolute;
    left: 858px;
    top: 112px;
    width: 66px;
    height: 66px;
    border: 4px solid var(--mark-grey);
  }
</style>
</head>
<body>
  <section class="card" aria-label="Cartão Ribeiro Tavares Advogados">
    <div class="card__divider"></div>
    <div class="card__info"></div>

    <div class="brand">
      <div class="brand__square"></div>
      <div class="brand__name">RIBEIRO TAVARES</div>
      <div class="brand__tagline">Advogados e Consultores</div>
    </div>

    <h1 class="person-name">Nome Completo</h1>

    <ul class="contact-list">
      <li class="contact-list__item">
        <svg class="contact-list__icon" viewBox="0 0 24 24" aria-hidden="true">
          <circle cx="12" cy="12" r="9" fill="none" stroke="var(--icon-grey)" stroke-width="2"/>
        </svg>
        (00) 0000-0000
      </li>
      <li class="contact-list__item">
        <svg class="contact-list__icon" viewBox="0 0 24 24" aria-hidden="true">
          <path d="M3 9c0-3 4-5 9-5s9 2 9 5l-3 1-2-3H8L6 10z" fill="var(--icon-grey)"/>
          <rect x="5" y="11" width="14" height="9" rx="2" fill="var(--icon-grey)"/>
          <circle cx="12" cy="15.5" r="2.2" fill="var(--card-white)"/>
        </svg>
        (00) 0000-0000
      </li>
      <li class="contact-list__item">
        <svg class="contact-list__icon" viewBox="0 0 24 24" aria-hidden="true">
          <g fill="none" stroke="var(--icon-grey)" stroke-width="1.8">
            <circle cx="12" cy="12" r="9"/>
            <ellipse cx="12" cy="12" rx="4" ry="9"/>
            <path d="M3 12h18M5 7h14M5 17h14"/>
          </g>
        </svg>
        www.seusite.com.br
      </li>
      <li class="contact-list__item">
        <svg class="contact-list__icon" viewBox="0 0 24 24" aria-hidden="true">
          <circle cx="12" cy="12" r="9" fill="none" stroke="var(--icon-grey)" stroke-width="2"/>
          <circle cx="12" cy="12" r="3.5" fill="var(--icon-grey)"/>
        </svg>
        @nome daempresa
      </li>
    </ul>

    <div class="faint-mark" aria-hidden="true"></div>
  </section>
</body>
</html>
```